Home web page re-vamp

I would like a stylish new home page design for a clients website.
I have included a sitemap to give some guidance.
The site needs to show off the design capabilitiesof the client

```html
<!DOCTYPE html>
<html lang="en">
<head>
<meta charset="utf-8">
<title>Company Name – Home</title>
<link href="https://fonts.googleapis.com/css2?family=Oswald:wght@300;400&family=Roboto:wght@400;500;700&family=Roboto+Condensed:wght@400&display=swap" rel="stylesheet">
<style>
  :root {
    --header-bg: rgba(30, 30, 32, 0.82);
    --hero-dark: #1b1a1e;
    --hero-mid: #3a2a28;
    --hero-warm: #7a3a1c;
    --white: #ffffff;
    --text-light: #d9d9d9;
    --text-muted: #c8c8c8;
    --accent-blue: #1b8fd6;
    --accent-orange: #e8600a;
    --card-top: #dcdcdc;
    --card-border: #d4d4d4;
    --heading-dark: #333333;
    --body-dark: #444444;
    --btn-top: #2a8fd4;
    --btn-bottom: #0b65a8;
    --footer-top: #2c2c2c;
    --footer-bottom: #1a1a1a;
    --footer-grey: #9a9a9a;
  }
  * { margin: 0; padding: 0; box-sizing: border-box; }
  html, body { width: 1200px; height: 900px; overflow: hidden; }
  body { position: relative; background: var(--white); font-family: 'Roboto', sans-serif; }

  .hero {
    position: absolute; left: 0; top: 0; width: 1200px; height: 527px;
    background:
      radial-gradient(ellipse 520px 160px at 720px 420px, rgba(150,60,20,0.55), transparent 70%),
      radial-gradient(ellipse 420px 120px at 260px 430px, rgba(120,50,20,0.45), transparent 70%),
      linear-gradient(180deg, #1e2026 0%, #2a2a31 35%, var(--hero-mid) 65%, #2b1d1a 85%, var(--hero-dark) 100%);
  }

  .site-header {
    position: absolute; left: 0; top: 0; width: 1200px; height: 52px;
    background: var(--header-bg);
  }
  .brand {
    position: absolute; left: 174px; top: 8px; height: 36px;
    display: flex; align-items: center; gap: 9px;
  }
  .brand-mark { width: 38px; height: 34px; background: var(--accent-blue); }
  .brand-name {
    font-family: 'Oswald', sans-serif; font-weight: 400; font-size: 31px;
    color: var(--white); letter-spacing: 0.2px; line-height: 1;
  }
  .main-nav {
    position: absolute; right: 174px; top: 0; height: 52px;
    display: flex; gap: 15px; align-items: center;
  }
  .main-nav a {
    position: relative; display: block; height: 52px; line-height: 55px;
    font-family: 'Roboto Condensed', sans-serif; font-size: 13px;
    color: var(--white); text-decoration: none; padding: 0 0;
  }
  .main-nav a.is-active { color: var(--accent-blue); }
  .main-nav a.is-active::after {
    content: ""; position: absolute; left: -7px; right: -7px; bottom: 0; height: 2px;
    background: var(--accent-blue);
  }

  .hero-kicker {
    position: absolute; left: 0; top: 128px; width: 1200px; text-align: center;
    font-family: 'Oswald', sans-serif; font-weight: 300; font-size: 29px; color: var(--text-muted);
  }
  .hero-title {
    position: absolute; left: 331px; top: 186px; width: 540px; height: 58px;
    border: 1px solid rgba(255,255,255,0.55); background: rgba(0,0,0,0.18);
    text-align: center; line-height: 56px;
    font-family: 'Oswald', sans-serif; font-weight: 400; font-size: 41px; color: var(--white);
  }
  .hero-lede {
    position: absolute; left: 0; top: 262px; width: 1200px; text-align: center;
    font-size: 15px; color: var(--text-light);
  }
  .hero-button {
    position: absolute; left: 523px; top: 331px; width: 155px; height: 41px;
    border: 1px solid rgba(255,255,255,0.6); background: rgba(0,0,0,0.25);
    text-align: center; line-height: 40px; text-decoration: none;
    font-family: 'Oswald', sans-serif; font-weight: 300; font-size: 27px; color: var(--white);
  }
  .scroll-cue { position: absolute; left: 577px; top: 412px; }

  .hero-divider {
    position: absolute; left: 0; top: 527px; width: 1200px; height: 3px; background: #d8d8d8;
  }

  .features { position: absolute; left: 174px; top: 565px; width: 852px; }
  .feature-card {
    position: absolute; top: 0; width: 196px; height: 176px;
    border: 1px solid var(--card-border); border-bottom: none;
    background: linear-gradient(180deg, var(--card-top) 0%, #f2f2f2 55%, var(--white) 100%);
    text-align: center;
  }
  .feature-icon { position: absolute; left: 72px; top: 18px; width: 52px; height: 52px; }
  .feature-title {
    position: absolute; left: 0; width: 100%; color: var(--heading-dark);
    font-weight: 500; font-size: 16.5px; line-height: 19.5px;
  }
  .feature-text {
    position: absolute; left: 0; top: 135px; width: 100%;
    font-size: 11px; line-height: 16.5px; color: var(--body-dark);
  }
  .feature-button {
    position: absolute; top: 187px; left: 59px; width: 79px; height: 22px;
    background: linear-gradient(180deg, var(--btn-top), var(--btn-bottom));
    border-radius: 2px; text-align: center; line-height: 22px; text-decoration: none;
    font-size: 9.5px; font-weight: 700; color: var(--white);
  }

  .site-footer {
    position: absolute; left: 0; top: 823px; width: 1200px; height: 77px;
    border-top: 3px solid #cfcfcf;
    background: linear-gradient(180deg, var(--footer-top), var(--footer-bottom));
  }
  .footer-nav {
    position: absolute; left: 174px; top: 21px; font-size: 11px; font-weight: 700; color: var(--white);
  }
  .footer-nav a { color: var(--white); text-decoration: none; }
  .footer-nav .sep { margin: 0 4px; font-weight: 400; }
  .copyright { position: absolute; left: 174px; top: 41px; font-size: 11px; color: var(--footer-grey); }
  .social { position: absolute; left: 876px; top: 26px; display: flex; gap: 7px; }
  .social span { width: 24px; height: 24px; border-radius: 50%; background: var(--white); display: block; }
</style>
</head>
<body>
  <div class="hero" role="img" aria-label="Blurred photograph of a suspension bridge over the bay at dusk, city lights glowing orange"></div>

  <header class="site-header">
    <div class="brand">
      <span class="brand-mark"></span>
      <span class="brand-name">COMPANY NAME</span>
    </div>
    <nav class="main-nav">
      <a class="is-active" href="#">Home</a>
      <a href="#">About Us</a>
      <a href="#">Services</a>
      <a href="#">Our Clients</a>
      <a href="#">Gallery</a>
      <a href="#">Health &amp; Safety</a>
      <a href="#">Specification Sheets</a>
      <a href="#">Contact Us</a>
    </nav>
  </header>

  <p class="hero-kicker">Lorem Ipsum</p>
  <h1 class="hero-title">SIMPLY DUMMY TEXT OF PRINTING</h1>
  <p class="hero-lede">It is a long established fact that a reader will be distracted by the readable content</p>
  <a class="hero-button" href="#">READ MORE</a>
  <svg class="scroll-cue" width="47" height="47" viewBox="0 0 47 47" aria-label="Scroll down">
    <circle cx="23.5" cy="23.5" r="22.5" fill="none" stroke="#ffffff" stroke-width="1.3"/>
    <polyline points="16,21 23.5,28 31,21" fill="none" stroke="#ffffff" stroke-width="1.5"/>
  </svg>

  <div class="hero-divider"></div>

  <section class="features">
    <article class="feature-card" style="left:0">
      <svg class="feature-icon" viewBox="0 0 52 52" aria-label="Information">
        <circle cx="26" cy="26" r="23" fill="none" stroke="var(--accent-orange)" stroke-width="4"/>
        <circle cx="26" cy="15" r="3.5" fill="var(--accent-orange)"/>
        <path d="M20 22h9v15h3.5v4h-12.5v-4h3.5v-11h-3.5z" fill="var(--accent-orange)"/>
      </svg>
      <h2 class="feature-title" style="top:94px">Why Us</h2>
      <p class="feature-text">7 Days from quotation to delivery<br>using the latest technology</p>
      <a class="feature-button" href="#">READ MORE</a>
    </article>

    <article class="feature-card" style="left:219px">
      <div class="feature-icon" role="img" aria-label="Illustration of an architect's drawing board" style="background:var(--accent-orange);opacity:.85;border-radius:2px"></div>
      <h2 class="feature-title" style="top:85px">Architects<br>&amp; Designers</h2>
      <p class="feature-text">Advice on colours and materials<br>Environmental friendly manufacture</p>
      <a class="feature-button" href="#">READ MORE</a>
    </article>

    <article class="feature-card" style="left:437px">
      <div class="feature-icon" role="img" aria-label="Illustration of a construction worker in a hard hat" style="background:var(--accent-orange);opacity:.85;border-radius:2px"></div>
      <h2 class="feature-title" style="top:85px">Commercial<br>Fit Out Companies</h2>
      <p class="feature-text">Site Surveys and Consultation by<br>our experienced design team</p>
      <a class="feature-button" href="#">READ MORE</a>
    </article>

    <article class="feature-card" style="left:656px">
      <div class="feature-icon" role="img" aria-label="Award medal with laurel wreath" style="background:var(--accent-orange);opacity:.85;border-radius:50%"></div>
      <h2 class="feature-title" style="top:85px">Awards<br>&amp; Accreditations</h2>
      <p class="feature-text">We are continually looking at how<br>we can improve our services</p>
      <a class="feature-button" href="#">READ MORE</a>
    </article>
  </section>

  <footer class="site-footer">
    <nav class="footer-nav">
      <a href="#">Home</a><span class="sep">|</span><a href="#">About Us</a><span class="sep">|</span><a href="#">Services</a><span class="sep">|</span><a href="#">Our Clients</a><span class="sep">|</span><a href="#">Gallery</a><span class="sep">|</span><a href="#">Health &amp; Safety</a><span class="sep">|</span><a href="#">Specification Sheets</a><span class="sep">|</span><a href="#">Contact Us</a>
    </nav>
    <p class="copyright">Copyright © 2014 Company Name. All Rights Reserved.</p>
    <div class="social" aria-label="Social links">
      <span aria-label="Social network link"></span>
      <span aria-label="Social network link"></span>
      <span aria-label="News feed link"></span>
      <span aria-label="Social network link"></span>
      <span aria-label="Video channel link"></span>
    </div>
  </footer>
</body>
</html>
```